Business Card Design

We need a design for business cards for our company. We have a logo. We teach EMT's and we are based out of Virginia. The information that will need to add would be, name, title, phone number, email, address. On the back of the business card would be "We help you, help others"

Target Market(s)

People that want to become EMT's

Colors

Designer to choose colors to be used in the design.

Requirements
Must have
• company logo

```html
<!DOCTYPE html>
<html lang="en">
<head>
<meta charset="utf-8">
<title>Medic Path Training – Business Cards</title>
<link rel="stylesheet" href="https://fonts.googleapis.com/css2?family=Montserrat:wght@400;500;700&display=swap">
<style>
  :root {
    --stage: #2e2f31;
    --card: #1f2b36;
    --red: #e3243f;
    --grey: #a3abb3;
    --grey-soft: #8d969e;
  }
  * { margin: 0; padding: 0; box-sizing: border-box; }
  html, body {
    width: 1200px; height: 1021px; overflow: hidden;
    background: var(--stage);
    font-family: "Montserrat", sans-serif;
  }
  .card {
    position: absolute; left: 250px;
    width: 700px; height: 400px;
    background: var(--card);
    box-shadow: 0 14px 30px rgba(0,0,0,.45);
  }
  .card--back { top: 70px; }
  .card--front { top: 551px; }

  .brand {
    position: absolute; left: 0; right: 0;
    display: flex; align-items: center; justify-content: center; gap: 14px;
    color: var(--red); font-weight: 700; font-size: 38px; letter-spacing: .5px;
  }
  .brand__dot { width: 18px; height: 18px; border-radius: 50%; background: var(--red); }
  .card--back .brand { top: 150px; }
  .card--front .brand { top: 80px; }

  .tagline {
    position: absolute; top: 262px; left: 0; right: 0; text-align: center;
    color: var(--grey); font-size: 15px; letter-spacing: 4px;
  }
  .tagline em { font-style: normal; color: var(--red); }

  .person {
    position: absolute; top: 210px; right: 372px; text-align: right;
  }
  .person__name { color: var(--red); font-weight: 700; font-size: 24px; }
  .person__title { color: var(--grey); font-size: 19px; margin-top: 2px; }

  .divider {
    position: absolute; left: 346px; top: 208px;
    width: 1px; height: 82px; background: var(--grey-soft);
  }

  .contact {
    position: absolute; left: 368px; top: 214px; list-style: none;
    color: var(--grey); font-size: 19px; line-height: 28px;
  }
  .contact li { display: flex; align-items: center; gap: 10px; }
  .contact svg { width: 17px; height: 17px; flex: none; }

  .address {
    position: absolute; left: 0; right: 0; top: 322px; text-align: center;
    color: var(--grey); font-size: 19px;
  }
</style>
</head>
<body>
  <section class="card card--back">
    <div class="brand"><span class="brand__dot"></span>Medic Path Training</div>
    <p class="tagline">WE HELP YOU, <em>HELP OTHERS</em></p>
  </section>

  <section class="card card--front">
    <div class="brand"><span class="brand__dot"></span>Medic Path Training</div>

    <div class="person">
      <p class="person__name">Daniel Carter</p>
      <p class="person__title">Founder</p>
    </div>

    <div class="divider"></div>

    <ul class="contact">
      <li>
        <svg viewBox="0 0 24 24" aria-hidden="true"><path fill="#e3243f" d="M6.6 10.8a15.5 15.5 0 0 0 6.6 6.6l2.2-2.2c.3-.3.7-.4 1-.2 1.1.4 2.3.6 3.6.6.6 0 1 .4 1 1V20c0 .6-.4 1-1 1A17 17 0 0 1 3 4c0-.6.4-1 1-1h3.5c.6 0 1 .4 1 1 0 1.3.2 2.5.6 3.6.1.3 0 .7-.2 1z"/></svg>
        (555) 318-2046
      </li>
      <li>
        <svg viewBox="0 0 24 24" aria-hidden="true"><rect x="2.5" y="5" width="19" height="14" fill="none" stroke="#e3243f" stroke-width="2"/><path d="M3 6l9 7 9-7" fill="none" stroke="#e3243f" stroke-width="2"/></svg>
        daniel@medicpath.com
      </li>
      <li>
        <svg viewBox="0 0 24 24" aria-hidden="true"><g fill="none" stroke="#e3243f" stroke-width="1.8"><circle cx="12" cy="12" r="9"/><ellipse cx="12" cy="12" rx="4" ry="9"/><path d="M3 12h18M5 7h14M5 17h14"/></g></svg>
        www.medicpathtraining.com
      </li>
    </ul>

    <p class="address">48 Harbor Lane, Richmond, Virginia, 23219</p>
  </section>
</body>
</html>
```